Set of 6 Print Ads for a Wind Farm

I'm looking for design of six separate print ads, each one sized 11.21”W x 22.21”T. Each one showcases a different benefit of the project - please see the uploaded PDF brief. I've included the fonts to use (Avenir family and AkzidGrtsk), as well as past examples for a little guidance. PLEASE DONT MIMIC THE SAMPLES. They should give you a feel and that's it. Choosing the right stock photography will be important given the size of the ads (which are all full-page). The audience for these ads is a small US Midwestern farming community.

Industry/Entity Type

Farm

Other font styles liked:
• Avenir family and AkzidGrtsk

Colors

Designer to choose colors to be used in the design.

Requirements
Must have
• separate designs for three full page print ads, per the brief

```html
<!DOCTYPE html>
<html lang="en">
<head>
<meta charset="utf-8">
<title>Wind Energy: A New Harvest for Clinton County</title>
<link rel="stylesheet" href="https://fonts.googleapis.com/css2?family=Oswald:wght@300&family=Nunito+Sans:ital,wght@0,400;0,700;0,800;1,400&display=swap">
<style>
  :root {
    --brand-red: #e3001b;
    --strip-grey: #efefee;
    --paper: #ffffff;
    --sand: #eeece8;
    --ink: #1c1c1c;
    --navy: #1d2f6f;
    --taupe: #8c8174;
    --white: #ffffff;
  }
  html, body {
    margin: 0;
    padding: 0;
    width: 1200px;
    height: 2376px;
    overflow: hidden;
    background: var(--paper);
  }
  .ad {
    position: relative;
    width: 1200px;
    height: 2376px;
    overflow: hidden;
    font-family: "Nunito Sans", "Avenir", sans-serif;
    color: var(--ink);
  }
  .top-band {
    position: absolute; left: 0; top: 0;
    width: 1200px; height: 66px;
    background: var(--brand-red);
  }
  .series-strip {
    position: absolute; left: 0; top: 66px;
    width: 1200px; height: 102px;
    background: var(--strip-grey);
  }
  .series-title {
    position: absolute; left: 60px; top: 30px;
    margin: 0;
    font-size: 28px; font-weight: 400;
    letter-spacing: 0.3px;
    color: var(--navy);
  }
  .turbine-photo {
    position: absolute; left: 862px; top: 4px;
    width: 338px; height: 94px;
    background: linear-gradient(180deg, #7fa6cf 0%, #b8cfe4 55%, #7e9a4f 78%, #5d7a33 100%);
  }
  .headline {
    position: absolute; left: 0; top: 190px;
    width: 1200px;
    margin: 0;
    text-align: center;
    font-family: "Oswald", "Arial Narrow", sans-serif;
    font-weight: 300;
    font-size: 82px;
    line-height: 128px;
    letter-spacing: 1px;
    text-transform: uppercase;
    color: var(--ink);
  }
  .hero-photo {
    position: absolute; left: 0; top: 606px;
    width: 1200px; height: 954px;
    background:
      radial-gradient(ellipse at 70% 20%, #b7c59a 0%, transparent 55%),
      linear-gradient(180deg, #c9c6bc 0%, #8c8672 45%, #5e5a4c 75%, #3d3a33 100%);
  }
  .benefit-panel {
    position: absolute; left: 0; top: 1560px;
    width: 1200px; height: 654px;
    background: var(--sand);
  }
  .benefit-copy {
    position: absolute; left: 0; top: 46px;
    width: 1200px;
    margin: 0;
    text-align: center;
    font-size: 52px;
    line-height: 64px;
    font-weight: 400;
    color: var(--ink);
  }
  .testimonial {
    position: absolute; left: 99px; top: 282px;
    width: 1034px; height: 336px;
    margin: 0;
  }
  .testimonial svg {
    position: absolute; left: 0; top: 0;
  }
  .testimonial-quote {
    position: absolute; left: 92px; top: 42px;
    width: 960px;
    margin: 0;
    font-style: italic;
    font-size: 57px;
    line-height: 58px;
    color: var(--white);
  }
  .testimonial-source {
    position: absolute; right: 99px; top: 158px;
    margin: 0;
    text-align: right;
    font-style: italic;
    font-size: 27px;
    line-height: 32px;
    color: var(--white);
  }
  .footer-band {
    position: absolute; left: 0; top: 2214px;
    width: 1200px; height: 162px;
    background: var(--brand-red);
    color: var(--white);
  }
  .brand-name {
    position: absolute; left: 55px; top: 22px;
    margin: 0;
    font-size: 118px;
    line-height: 120px;
    font-weight: 800;
    letter-spacing: 1px;
    color: var(--white);
  }
  .footer-tagline {
    position: absolute; left: 420px; top: 22px;
    margin: 0;
    font-size: 28px;
    line-height: 30px;
    font-weight: 800;
  }
  .footer-contact {
    position: absolute; left: 420px; top: 98px;
    margin: 0;
    font-size: 26px;
    line-height: 32px;
    font-weight: 400;
  }
</style>
</head>
<body>
<main class="ad">
  <div class="top-band"></div>

  <header class="series-strip">
    <p class="series-title">WIND ENERGY: A NEW HARVEST FOR CLINTON COUNTY</p>
    <div class="turbine-photo" role="img" aria-label="Photo of wind turbines on a green field under a blue sky"></div>
  </header>

  <h1 class="headline">Tens of millions in wind energy<br>investments will open doors<br>for Clinton County</h1>

  <div class="hero-photo" role="img" aria-label="Photo of smiling local shop owners in aprons beside a produce stand and a chalkboard sign reading Grand Opening, Welcome, Please come in"></div>

  <section class="benefit-panel">
    <p class="benefit-copy">Local spending on supplies and services<br>will help local businesses,<br>benefiting everyone in Clinton County.</p>

    <figure class="testimonial">
      <svg width="1034" height="336" viewBox="0 0 1034 336" aria-hidden="true">
        <polygon fill="var(--taupe)" points="6,14 40,4 78,12 120,2 170,10 214,4 262,12 310,3 360,11 410,5 458,13 506,2 556,10 604,4 652,12 700,3 748,11 796,5 846,13 894,4 944,11 990,3 1028,12 1022,60 1032,110 1024,160 1032,210 1022,262 1030,330 984,322 936,332 886,324 838,334 790,324 740,332 690,322 640,332 590,324 540,334 490,324 440,332 390,322 340,332 290,324 240,334 190,324 140,332 90,322 40,332 4,324 12,270 2,220 10,170 2,120 12,70"/>
      </svg>
      <blockquote class="testimonial-quote">“Bringing wind into our area was a huge bonus for us.” –</blockquote>
      <figcaption class="testimonial-source">Daniel Harlow,<br>Benton County<br>Economic Development Department<br>Director</figcaption>
    </figure>
  </section>

  <footer class="footer-band">
    <p class="brand-name">veyra</p>
    <p class="footer-tagline">A stronger economy. Yet another way a Veyra wind farm<br>will benefit all of Clinton County.</p>
    <p class="footer-contact">(555) 014-2280 – hello@clintonfieldwind.org</p>
  </footer>
</main>
</body>
</html>
```